TKR Capability Statement Brochure

We need a four or six-page flyer/brochure for our capability statement. This should include all the key written copy and photos/descriptions of the personnel, plus contact addresses in the current capability statement which is attached. We are looking for a modern, professional design that matches our professional approach to our business. Please incorporate our logo into the design.

Target Market(s)

Government departments, shipping companies, port operators, lawyers, export and import businesses, commodity companies.

Industry/Entity Type

Business Consultant

Contact Information for Business Card

Professional, simple to read, uncomplicated.

Font styles to use
Serif
Sans Serif

Colors

Designer to choose colors to be used in the design.

Requirements
Must have
• Company logo
• KEY MESSAGE: Providing independent, expert, confidential and professional services.
• Description of company
• Description and photos of personnel.
• Contact details.
Should not have
• No cliches

```html
<!DOCTYPE html>
<html lang="en">
<head>
<meta charset="utf-8">
<title>TKR Capability Statement 2018</title>
<link rel="stylesheet" href="https://fonts.googleapis.com/css2?family=Open+Sans:ital,wght@0,400;0,600;0,700;0,800;1,400&display=swap">
<style>
:root{
  --bg:#3b3b3b;
  --paper:#ffffff;
  --navy:#2c4d7a;
  --blue:#3e6796;
  --blue-light:#5a82b0;
  --gold:#e6b21c;
  --ink:#4a4a4a;
  --ink-soft:#6d6d6d;
  --rule:#c9d3df;
}
*{box-sizing:border-box;margin:0;padding:0}
html,body{width:1026px;height:1200px;overflow:hidden;background:var(--bg)}
body{font-family:"Open Sans",Arial,sans-serif;color:var(--ink);position:relative}
.spread{position:absolute;left:103px;width:820px;height:580px;display:flex;box-shadow:0 6px 18px rgba(0,0,0,.45)}
.spread--outside{top:14px}
.spread--inside{top:606px}
.page{position:relative;flex:0 0 410px;width:410px;height:580px;background:var(--paper);overflow:hidden}
.page--left{box-shadow:inset -6px 0 10px -6px rgba(0,0,0,.18)}
.page--right{box-shadow:inset 6px 0 10px -6px rgba(0,0,0,.18)}
p{font-size:6.6px;line-height:1.5;color:var(--ink)}
.brand{display:flex;align-items:center;gap:6px;font-weight:800;color:var(--navy);letter-spacing:.5px}
.brand__mark{width:14px;height:14px;background:var(--navy)}
.brand--light{color:#fff}
.brand--light .brand__mark{background:#fff}

/* back cover */
.overview{position:absolute;left:28px;top:34px;right:28px}
.overview__title{font-size:9px;font-weight:800;color:var(--navy);letter-spacing:.4px;margin-bottom:8px}
.overview__cols{display:grid;grid-template-columns:1fr 1fr;gap:16px}
.overview__cols p{margin-bottom:7px;text-align:justify}
.back-footer{position:absolute;left:28px;right:28px;top:340px;display:grid;grid-template-columns:1fr 1fr;gap:16px;border-top:1px solid var(--rule);padding-top:18px}
.back-footer .brand{font-size:30px;margin-bottom:12px}
.back-footer .brand__mark{width:26px;height:26px}
.company{font-size:7.4px;font-weight:700;color:var(--navy);line-height:1.45}
.company__abn{margin:8px 0}
.company__addr{font-weight:400;color:var(--ink);font-size:6.8px;line-height:1.5}
.company__addr b{color:var(--blue)}
.contact-line{display:flex;align-items:center;gap:4px;font-weight:400;font-size:6.8px;color:var(--ink)}
.contact-line svg{width:7px;height:7px;fill:var(--blue)}
.region{margin-bottom:7px}
.region__state{font-size:6.8px;font-weight:700;color:var(--gold);letter-spacing:.3px}
.region__person{display:grid;grid-template-columns:64px 1fr;font-size:6.6px;line-height:1.5}
.region__name{font-weight:700;color:var(--navy)}

/* front cover */
.cover__band{position:absolute;left:0;top:0;width:96px;height:100%;background:linear-gradient(180deg,var(--blue) 0%,var(--navy) 100%)}
.cover__title{position:absolute;left:48px;bottom:70px;transform-origin:left center;transform:rotate(-90deg) translateY(-50%);white-space:nowrap;font-size:30px;color:#fff;font-weight:400;letter-spacing:-.3px}
.cover__title span{color:var(--gold);font-weight:700}
.page--cover .brand{position:absolute;left:190px;top:34px;font-size:30px}
.page--cover .brand__mark{width:26px;height:26px}
.cover__photo{position:absolute;left:96px;top:96px;right:0;height:290px;background:linear-gradient(180deg,#e9eef4 0%,#b9c6d4 45%,#6f859d 62%,#9fb3c6 100%)}
.cover__tag{position:absolute;left:120px;top:410px;right:24px}
.cover__tag h1{font-size:15px;font-weight:800;color:#333;letter-spacing:.4px}
.cover__tag h2{font-size:11px;font-weight:400;color:var(--blue);margin-top:2px}
.cover__web{position:absolute;left:120px;top:470px;font-size:7.5px;letter-spacing:2.4px;color:var(--ink-soft)}

/* competencies */
.core__panel{position:absolute;left:0;top:0;width:186px;height:100%;background:linear-gradient(180deg,var(--blue) 0%,var(--navy) 100%)}
.core__photo{position:absolute;left:0;bottom:0;width:186px;height:250px;background:linear-gradient(180deg,rgba(62,103,150,0) 0%,rgba(120,150,185,.35) 55%,rgba(44,77,122,.6) 100%)}
.core__panel .brand{position:absolute;left:22px;top:120px;font-size:30px}
.core__panel .brand__mark{width:26px;height:26px}
.core__heading{position:absolute;left:22px;top:170px;right:12px}
.core__heading h2{font-size:19px;font-weight:700;color:var(--gold);line-height:1.1}
.core__heading p{font-size:9px;color:#fff;line-height:1.35;margin-top:3px}
.core__lists{position:absolute;left:198px;top:22px;right:10px}
.core__group{margin-bottom:9px}
.core__group h3{font-size:7.6px;font-weight:800;color:var(--navy);margin-bottom:3px;letter-spacing:.2px}
.ticks{list-style:none}
.ticks li{position:relative;padding-left:11px;font-size:6.2px;line-height:10.2px;color:var(--ink);white-space:nowrap;overflow:hidden;text-overflow:clip}
.ticks li::before{content:"";position:absolute;left:0;top:2px;width:6px;height:6px;border:1px solid var(--blue-light);border-radius:50%}
.ticks li::after{content:"";position:absolute;left:2.5px;top:3.3px;width:1.4px;height:2.6px;border:solid var(--blue);border-width:0 1px 1px 0;transform:rotate(45deg)}

/* team */
.team{position:absolute;left:20px;top:22px;right:20px}
.team__title{font-size:8.6px;font-weight:800;color:var(--navy)}
.team__intro{font-size:6.2px;margin:3px 0 7px}
.team__sub{font-size:8px;font-weight:700;color:var(--blue);margin-bottom:8px;border-bottom:1px solid var(--rule);padding-bottom:4px}
.team__grid{display:grid;grid-template-columns:1fr 1fr;gap:0 14px}
.bio{display:grid;grid-template-columns:42px 1fr;gap:6px;margin-bottom:12px}
.bio__photo{width:40px;height:40px;border-radius:50%;border:2px solid var(--blue-light);background:linear-gradient(160deg,#d6dde6 0%,#97a8bb 100%)}
.bio__name{font-size:7.2px;font-weight:700;color:var(--navy);margin-bottom:2px}
.bio p{font-size:6px;line-height:1.45;text-align:justify}
.clients h3{font-size:8px;font-weight:800;color:var(--navy);margin-bottom:3px}
.clients p{font-size:6px;text-align:justify;margin-bottom:5px}
.clients .lead{font-weight:700;color:var(--blue)}
</style>
</head>
<body>

<section class="spread spread--outside">
  <article class="page page--left page--back">
    <div class="overview">
      <h2 class="overview__title">COMPANY OVERVIEW</h2>
      <div class="overview__cols">
        <div>
          <p>Established in 2009, Tasman Keel Resources (TKR) has offices in Victoria, New South Wales, Queensland and Tasmania and aims to position itself as the leading maritime consultancy in the region.</p>
          <p>The TKR team brings together extensive commercial experience and expertise to adopt a highly business-focused approach to any technical and operational analysis it undertakes within the maritime and ports sectors.</p>
          <p>TKR has an international network of associates, including strategic partnerships with global data providers, shipbrokers and financial market specialists, together with leading members of international shipping exchanges.</p>
          <p>TKR provides shipping, transportation and marine industry services to supplement and support our clients' requirements and strategies. We provide independent, expert, confidential and professional services using reliable, dedicated, highly experienced and qualified consultants and analysts who work to fully understand customer needs and requirements and provide the agreed service deliverables on time and on budget.</p>
        </div>
        <div>
          <p>TKR is able to step in to a client's existing organisation and supply the skill, knowledge and services to supplement or support an existing marine operation or port project. We can also apply our expertise in support of the preparation of a submission to a tribunal or legal process.</p>
          <p>Tasman Keel Resources is a member of the industry bodies for freight, trade and maritime affairs, and individual directors of TKR are members of the professional institutes for master mariners, shipbrokers and logistics and transport.</p>
          <p>You can count on our professional team to expertly cater to all of your commercial marine requirements. With management experience at the highest levels and an extensive combined skills and knowledge set, our team is unrivalled in the region. From ship acquisition and chartering to operational, logistics and economic assessments, as well as targeted industry training, crisis and media management, Tasman Keel Resources has the dependable, efficient and cost effective solutions your business needs.</p>
        </div>
      </div>
    </div>
    <div class="back-footer">
      <div>
        <div class="brand"><span class="brand__mark"></span>TKR</div>
        <div class="company">
          Tasman Keel Resources Pty Ltd.<br>ATF TKR Group Unit Trust
          <div class="company__abn">ABN: 00 000 000 000</div>
          <div class="company__addr">
            <b>Registered Address:</b><br>Tasman Keel Resources Pty Ltd.<br>42 Harbour Lane,<br>Portside, Victoria 3900.
          </div>
          <div style="margin-top:6px">
            <div class="contact-line"><svg viewBox="0 0 10 10"><path d="M2 1l2 0 1 2-1 1c.6 1.2 1.4 2 2.6 2.6l1-1 2 1v2c0 .6-.4 1-1 1C4.5 9.6.4 5.5 1 2c0-.6.4-1 1-1z"/></svg>+61 3 9000 1122</div>
            <div class="contact-line"><svg viewBox="0 0 10 10"><rect x="1" y="3" width="8" height="5"/><rect x="3" y="1" width="4" height="2"/></svg>+61 3 9000 3344</div>
            <div class="contact-line"><svg viewBox="0 0 10 10"><path d="M1 2h8v6H1z M1 2l4 3 4-3"/></svg>office@tkrmarine.example</div>
          </div>
        </div>
      </div>
      <div>
        <div class="region"><div class="region__state">VICTORIA</div>
          <div class="region__person"><span class="region__name">Ray Linden</span><span>ray@tkrmarine.example</span></div>
          <div class="region__person"><span>+61 400 111 201</span><span></span></div>
          <div class="region__person"><span class="region__name">Sadie Garner</span><span>sadie@tkrmarine.example</span></div>
          <div class="region__person"><span>+61 400 111 202</span><span></span></div>
        </div>
        <div class="region"><div class="region__state">NEW SOUTH WALES</div>
          <div class="region__person"><span class="region__name">Paul Brennan</span><span>paul@tkrmarine.example</span></div>
          <div class="region__person"><span>+61 400 111 203</span><span></span></div>
        </div>
        <div class="region"><div class="region__state">TASMANIA</div>
          <div class="region__person"><span class="region__name">Colin Mercer</span><span>colin@tkrmarine.example</span></div>
          <div class="region__person"><span>+61 400 111 204</span><span></span></div>
        </div>
        <div class="region"><div class="region__state">QUEENSLAND</div>
          <div class="region__person"><span class="region__name">Stuart Rowe</span><span>stuart@tkrmarine.example</span></div>
          <div class="region__person"><span>+61 400 111 205</span><span></span></div>
        </div>
      </div>
    </div>
  </article>

  <article class="page page--right page--cover">
    <div class="cover__band"></div>
    <div class="cover__title">Capability Statement <span>2018</span></div>
    <div class="brand"><span class="brand__mark"></span>TKR</div>
    <div class="cover__photo" role="img" aria-label="City skyline across a harbour with port cranes and calm water"></div>
    <div class="cover__tag">
      <h1>PROVIDING INDEPENDENT,</h1>
      <h2>expert, confidential and professional services</h2>
    </div>
    <div class="cover__web">www.tkrmarine.example</div>
  </article>
</section>

<section class="spread spread--inside">
  <article class="page page--left page--core">
    <div class="core__panel">
      <div class="core__photo" role="img" aria-label="Faint harbour and industrial skyline in blue tones"></div>
      <div class="brand brand--light"><span class="brand__mark"></span>TKR</div>
      <div class="core__heading">
        <h2>Core Competencies</h2>
        <p>TKR has demonstrable experience in the following areas:</p>
      </div>
    </div>
    <div class="core__lists">
      <div class="core__group">
        <h3>Commercial maritime trade</h3>
        <ul class="ticks">
          <li>Operational knowledge of all major shipping trades</li>
          <li>Thorough understanding of marine, ports and logistics policy</li>
          <li>Reviews of commercial maritime operations</li>
          <li>Evaluation and management of tenders and proposals</li>
          <li>Feasibility studies (commercial and operational)</li>
          <li>Reviews of commercial maritime operations</li>
          <li>Advice on joint venture issues and development</li>
          <li>Fleet availability and trade sector forecasting</li>
          <li>Industry education and training</li>
          <li>Topical industry workshops</li>
          <li>Expert witness</li>
        </ul>
      </div>
      <div class="core__group">
        <h3>SHIP MANAGEMENT</h3>
        <ul class="ticks">
          <li>Vessel ownership and management</li>
          <li>Vessel chartering and operational management</li>
          <li>Vessel sales and purchase</li>
          <li>Advice on ship charter parties</li>
          <li>Re-engineering of marine departments</li>
          <li>Innovative improvements to marine systems</li>
          <li>Management of suppliers and resources</li>
          <li>Analysing shipping and logistic requirements</li>
          <li>Meeting charterers' needs from acquisition to delivery</li>
        </ul>
      </div>
      <div class="core__group">
        <h3>PORTS &amp; RELATED INDUSTRY</h3>
        <ul class="ticks">
          <li>Modelling and optimisation of port throughputs</li>
          <li>Matching port infrastructure to commodity types</li>
          <li>Management of port loading and unloading terminals</li>
          <li>Planning and management of the ship/shore interface</li>
          <li>Port efficiency assessments</li>
          <li>Modelling port use using queue theory</li>
          <li>Planning and forecasting aggregate demurrage</li>
          <li>Assessments of port and marine safety and security</li>
          <li>Risk assessments of marine and port operations</li>
          <li>Reviews of navigation and marine safety</li>
          <li>Emergency and crisis management</li>
        </ul>
      </div>
      <div class="core__group">
        <h3>SUPPLY CHAIN</h3>
        <ul class="ticks">
          <li>Supply chain evaluation and optimisation</li>
          <li>Evaluation and management of tenders and proposals</li>
          <li>Marine project management and support</li>
          <li>Management of bulk and breakbulk logistics</li>
          <li>Stacking analysis for bulk terminals</li>
          <li>Re-engineering of supply chains</li>
        </ul>
      </div>
    </div>
  </article>

  <article class="page page--right page--team">
    <div class="team">
      <h2 class="team__title">Tasman Keel Resources Team :</h2>
      <p class="team__intro">All team members have decades of commercial shipping industry experience at senior levels and have substantial relevant specialist expertise to offer. With backgrounds in many parts of the industry, the TKR team brings together a capacity to deliver practical solutions to complex marine and port projects.</p>
      <h3 class="team__sub">The TKR management team comprises:</h3>
      <div class="team__grid">
        <div>
          <div class="bio">
            <div class="bio__photo" role="img" aria-label="Portrait of Paul Brennan"></div>
            <div><div class="bio__name">Paul Brennan</div>
              <p>Based in Sydney, Paul was, prior to joining TKR, general manager shipping for a major building materials group for many years. His responsibilities included managing owned and chartered ships and the transport of raw materials. He is a Master Mariner with an MSc in logistics and has held senior roles with industry associations and port advisory boards.</p></div>
          </div>
          <div class="bio">
            <div class="bio__photo" role="img" aria-label="Portrait of Ray Linden"></div>
            <div><div class="bio__name">Ray Linden</div>
              <p>Based in Melbourne, Ray is a Master Mariner and holds an MBA. He has over 40 years of experience in the shipping industry. A founding member of TKR, he previously directed bulk shipping operations and led the development of marine logistics strategies for major commodity projects, analysing supply and demand scenarios and business cases.</p></div>
          </div>
          <div class="bio">
            <div class="bio__photo" role="img" aria-label="Portrait of Stuart Rowe"></div>
            <div><div class="bio__name">Stuart Rowe</div>
              <p>Based in Brisbane, Stuart has a seafaring background and over 40 years of commercial shipping experience. A Fellow of the institute of shipbrokers and a founding director of TKR, he has managed many passenger, ship and cargo operations. As principal of Southwind Chartering since 1985, Stuart has extensive knowledge of commercial shipping and operational matters.</p></div>
          </div>
        </div>
        <div>
          <div class="bio">
            <div class="bio__photo" role="img" aria-label="Portrait of Sadie Garner"></div>
            <div><div class="bio__name">Sadie Garner</div>
              <p>Based in Melbourne, Sadie has more than 40 years experience in the international maritime and transport industry, including work with global traders. As a leading industry analyst, she has advised government agencies, port operators, terminals and shipping companies, and edited a respected regional shipping directory.</p></div>
          </div>
          <div class="bio">
            <div class="bio__photo" role="img" aria-label="Portrait of Colin Mercer"></div>
            <div><div class="bio__name">Colin Mercer</div>
              <p>Based in Hobart, Colin commenced his maritime career as a deck officer, gaining a broad range of experience in many shipping sectors up to senior management level. He has worked across ship management, operations and training, and developed safety management systems and qualifications for the industry.</p></div>
          </div>
          <div class="clients">
            <h3>CLIENTS :</h3>
            <p>TKR's clientele includes government agencies, oil and gas operators, resource companies, ports, shipping and shipper interests, as well as financial institutions and business consultancies. TKR specialises in commercial marine advice and the provision of management support in high-value marine projects for several government departments.</p>
            <p class="lead">TKR has acted as broker for significant multimillion-dollar ship acquisitions for the nation and provided advice and analysis on projects ranging from market research through to sale of surplus marine assets.</p>
          </div>
        </div>
      </div>
    </div>
  </article>
</section>

</body>
</html>
```